" Empresa em abertura de firma (status), voltada para o segmento de Headhunter / Jobhunter, Coaching e demais serviços administrativos/treinamento relacionados. "

```html
<!DOCTYPE html>
<html lang="pt-BR">
<head>
<meta charset="UTF-8">
<title>PrimeStaff – Cartão de visita</title>
<link href="https://fonts.googleapis.com/css2?family=Montserrat:wght@400;500;600;700&display=swap" rel="stylesheet">
<style>
  :root {
    --bg: #e6e8ea;
    --card: #ffffff;
    --brand-blue: #1f5fa8;
    --sky: #3b8fd6;
    --green: #7cb83a;
    --gold: #d7a93a;
    --magenta: #c2368f;
    --purple: #7b4fa0;
    --text-gray: #6b6f75;
    --text-dark: #3a3d42;
    --shadow: rgba(0, 0, 0, 0.12);
  }
  * { margin: 0; padding: 0; box-sizing: border-box; }
  html, body {
    width: 1200px;
    height: 1200px;
    overflow: hidden;
    background: var(--bg);
    font-family: "Montserrat", sans-serif;
  }
  .sheet {
    width: 1200px;
    height: 1200px;
    display: flex;
    flex-direction: column;
    align-items: center;
    justify-content: center;
    gap: 60px;
  }
  .card {
    position: relative;
    width: 900px;
    height: 515px;
    background: var(--card);
    border-radius: 36px;
    overflow: hidden;
    box-shadow: 0 10px 30px var(--shadow);
  }

  /* Front */
  .front-art {
    position: absolute;
    left: 40px;
    top: 60px;
    width: 270px;
    height: 395px;
    border-radius: 20px;
    background: linear-gradient(180deg, #c9dcae 0%, #e7d3a2 50%, #b7d0e8 100%);
  }
  .brand {
    position: absolute;
    left: 400px;
    top: 220px;
    display: flex;
    align-items: center;
    gap: 18px;
  }
  .brand-dot {
    width: 34px;
    height: 34px;
    border-radius: 50%;
    background: var(--brand-blue);
  }
  .brand-name {
    font-size: 62px;
    font-weight: 600;
    color: var(--brand-blue);
    letter-spacing: -1px;
    line-height: 1;
  }

  /* Back */
  .back-art {
    position: absolute;
    right: 40px;
    top: 40px;
    width: 240px;
    height: 260px;
    border-radius: 20px;
    background: linear-gradient(180deg, #e3b8d4 0%, #cfe0b8 55%, #b7d0e8 100%);
  }
  .identity {
    position: absolute;
    left: 60px;
    top: 70px;
  }
  .identity-name {
    font-size: 30px;
    font-weight: 600;
    color: var(--green);
    letter-spacing: 1px;
  }
  .identity-role {
    font-size: 20px;
    font-weight: 500;
    color: var(--text-gray);
    margin-top: 4px;
  }
  .contacts {
    position: absolute;
    left: 60px;
    top: 250px;
    list-style: none;
    display: flex;
    flex-direction: column;
    gap: 14px;
  }
  .contact {
    display: flex;
    align-items: center;
    gap: 14px;
    font-size: 18px;
    font-weight: 500;
    color: var(--text-dark);
    line-height: 1.25;
  }
  .contact-icon {
    flex: 0 0 30px;
    width: 30px;
    height: 30px;
  }
</style>
</head>
<body>
<main class="sheet">

  <section class="card card-front">
    <div class="front-art" role="img" aria-label="Área da ilustração de pessoas em verde, dourado e azul"></div>
    <div class="brand">
      <span class="brand-dot"></span>
      <span class="brand-name">PrimeStaff</span>
    </div>
  </section>

  <section class="card card-back">
    <div class="back-art" role="img" aria-label="Área da ilustração de pessoas em magenta, verde e azul"></div>

    <div class="identity">
      <p class="identity-name">NOME COMPLETO</p>
      <p class="identity-role">Cargo ou Função</p>
    </div>

    <ul class="contacts">
      <li class="contact">
        <svg class="contact-icon" viewBox="0 0 30 30" aria-hidden="true">
          <circle cx="15" cy="15" r="15" fill="var(--brand-blue)"/>
          <path d="M10.5 8.5 l3 0 l1 4 l-2 1.3 a8 8 0 0 0 3.7 3.7 l1.3 -2 l4 1 l0 3 a2 2 0 0 1 -2 2 A12 12 0 0 1 8.5 10.5 a2 2 0 0 1 2 -2z" fill="#fff"/>
        </svg>
        <span>(00) 0000-0000 | (00) 00000-0000</span>
      </li>
      <li class="contact">
        <svg class="contact-icon" viewBox="0 0 30 30" aria-hidden="true">
          <circle cx="15" cy="15" r="15" fill="var(--magenta)"/>
          <rect x="8" y="10" width="14" height="10" rx="1.5" fill="#fff"/>
          <path d="M8.5 10.8 L15 15.5 L21.5 10.8" fill="none" stroke="var(--magenta)" stroke-width="1.5"/>
        </svg>
        <span>seuemail@email.com</span>
      </li>
      <li class="contact">
        <svg class="contact-icon" viewBox="0 0 30 30" aria-hidden="true">
          <circle cx="15" cy="15" r="15" fill="var(--green)"/>
          <path d="M15 7 a5.5 5.5 0 0 1 5.5 5.5 c0 4 -5.5 10 -5.5 10 s-5.5 -6 -5.5 -10 A5.5 5.5 0 0 1 15 7z" fill="#fff"/>
          <circle cx="15" cy="12.5" r="2" fill="var(--green)"/>
        </svg>
        <span>Rua nome da rua, 00, bairro,<br>Cidade - Estado e CEP</span>
      </li>
      <li class="contact">
        <svg class="contact-icon" viewBox="0 0 30 30" aria-hidden="true">
          <circle cx="15" cy="15" r="15" fill="var(--gold)"/>
        </svg>
        <span>@primestaff</span>
      </li>
    </ul>
  </section>

</main>
</body>
</html>
```